Business Card - Professional Minimalist - Double sided

We appreciate minimalist logo/web/collateral designs that allow design to tell a story. We want to relay a professional image/approach but throwing in a splash of modern when we’re able so long as it’s not distracting. Think 75% classic corporate, 25% modern. Open to black or white design, not sure which might look the best.

Target Market(s)

Senior executives or related government affairs contacts within the agriculture, energy, and defense industries (i.e., potential clients) but located outside of Washington, DC. Most potential clients based in DC with be familiar with both of us and our shared history.

Industry/Entity Type

Consulting

Contact Information for Business Card

Name: Daniel R. Whitlock
Title: Co-Founder & Partner
Address: 418 Bramblewood Ave. SE | Suite 2716 | Washington, D.C. 20019
Phone: (202) 555-0187
Email: Daniel@HollerbyWhitlock.com

Font styles to use
Serif

Colors

Designer to choose only greyscale colors for use in the design.

Requirements
Must have
• Name: Daniel R. Whitlock
Phone: (202) 555-0187

```html
<!DOCTYPE html>
<html lang="en">
<head>
<meta charset="utf-8">
<title>Hollerby Whitlock Group — Business Card</title>
<link href="https://fonts.googleapis.com/css2?family=Marcellus&family=Open+Sans:wght@400;700&display=swap" rel="stylesheet">
<style>
  :root {
    --backdrop: #9b9b9b;
    --card-dark: #4c4c4c;
    --card-dark-tone: #454545;
    --mark-light: #b4b4b4;
    --card-light: #ececec;
    --ink: #4a4a4a;
    --ink-soft: #5a5a5a;
    --icon: #8e8e8e;
    --rule: #9a9a9a;
  }
  * { margin: 0; padding: 0; box-sizing: border-box; }
  html, body {
    width: 1200px; height: 900px; overflow: hidden;
    background: var(--backdrop);
    font-family: "Open Sans", sans-serif;
  }
  .canvas { position: relative; width: 1200px; height: 900px; }
  .card { position: absolute; left: 363px; width: 475px; height: 270px; }

  .card-back { top: 145px; background: var(--card-dark); overflow: hidden; }
  .pattern-area {
    position: absolute; inset: 0;
    background: linear-gradient(135deg, var(--card-dark) 0%, var(--card-dark-tone) 100%);
  }
  .back-mark {
    position: absolute; left: 395px; top: 193px;
    width: 52px; height: 52px;
    background: var(--mark-light);
  }

  .card-front { top: 484px; background: var(--card-light); color: var(--ink); }
  .brand {
    position: absolute; left: 26px; top: 26px;
    display: flex; align-items: center; gap: 10px;
  }
  .brand-square { width: 36px; height: 36px; background: var(--ink-soft); flex: none; }
  .brand-name {
    font-family: "Marcellus", serif;
    font-size: 18px; font-weight: 400; letter-spacing: 0.8px;
    color: var(--ink-soft); text-transform: uppercase; white-space: nowrap;
  }

  .person { position: absolute; right: 26px; top: 150px; text-align: right; }
  .person-name {
    font-size: 14.5px; font-weight: 700; letter-spacing: 0.3px;
    text-transform: uppercase; line-height: 18px; color: var(--ink);
  }
  .person-title { font-size: 11.5px; font-weight: 400; line-height: 17px; color: var(--ink-soft); }

  .divider { position: absolute; left: 26px; right: 26px; top: 192px; height: 1px; background: var(--rule); }

  .contact-list { position: absolute; left: 26px; top: 202px; list-style: none; }
  .contact-list li {
    display: flex; align-items: center; gap: 8px;
    font-size: 11.5px; line-height: 15.3px; color: var(--ink-soft); white-space: nowrap;
  }
  .contact-list svg { width: 9px; height: 9px; fill: var(--icon); flex: none; }
  .address {
    position: absolute; right: 26px; top: 202px; text-align: right;
    font-size: 11.5px; line-height: 15.3px; color: var(--ink-soft); font-style: normal; white-space: nowrap;
  }
</style>
</head>
<body>
<main class="canvas">
  <section class="card card-back">
    <div class="pattern-area" role="img" aria-label="Tonal repeating brand pattern on dark grey card back"></div>
    <span class="back-mark" aria-hidden="true"></span>
  </section>

  <section class="card card-front">
    <div class="brand">
      <span class="brand-square" aria-hidden="true"></span>
      <span class="brand-name">Hollerby Whitlock Group</span>
    </div>

    <div class="person">
      <p class="person-name">Daniel R. Whitlock</p>
      <p class="person-title">Co-Founder &amp; Partner</p>
    </div>

    <div class="divider"></div>

    <ul class="contact-list">
      <li>
        <svg viewBox="0 0 10 10" aria-hidden="true"><path d="M2 0.5 L3.6 2.6 L2.8 3.6 Q4 6 6.4 7.2 L7.4 6.4 L9.5 8 L8.4 9.5 Q4 9 0.5 1.6 Z"/></svg>
        (202) 555-0187
      </li>
      <li>
        <svg viewBox="0 0 10 10" aria-hidden="true"><path d="M0.5 2 H9.5 V8 H0.5 Z M1.2 2.6 L5 5.4 L8.8 2.6 V3.3 L5 6.1 L1.2 3.3 Z" fill-rule="evenodd"/></svg>
        Daniel@HollerbyWhitlock.com
      </li>
      <li>
        <svg viewBox="0 0 10 10" aria-hidden="true"><circle cx="5" cy="5" r="4.5"/><path d="M0.5 5 H9.5 M5 0.5 V9.5" stroke="#ececec" stroke-width="0.6"/></svg>
        HollerbyWhitlock.com
      </li>
    </ul>

    <address class="address">
      418 Bramblewood Ave. SE<br>
      Suite 2716<br>
      Washington, D.C. 20019
    </address>
  </section>
</main>
</body>
</html>
```